御城印はほぼ形式が決まっており、
サイズは幅105mm×高さ160mmで、ハガキより少し縦長になります。
文言などはほぼ定型で、内容は「記載項目」に表記します。

記載項目
文言は、

国指定史跡
対馬
鷹巣岳城
令和 年 月 日

で、鷹巣岳城の背景に家紋(対馬菅氏の場合、四ツ目結)になります。
テキストは黒の筆文字が多く、家紋は朱色が多いです。
目的・デザインなどの参考に、以前作成した御城印の記事をリンクします。

楢崎城跡の「御城印」を作成 汐凪観光物産協会(長崎新聞2019/12/06)
https://hanabosi-kiji.example/839201457362018495
幅105mm×高さ160mm

御城印はほぼ様式が決まっており、アレンジが難しかったと思いますが、文字のフォント・サイズ・配置、家紋の加工や配置、背景画像等の提案、全体のバランス等を考慮し、決定いたしました。

今回2度目のデザミールの利用でしたが、力作ぞろいの個性的な提案をいただき、感謝申し上げます。
前回はWEBサイト制作、今回は御城印でしたが、リーフレットなど各種デザインをご依頼することもあると思います。
ありがとうございました。
今後ともよろしくお願いいたします。

```html
<!DOCTYPE html>
<html lang="ja">
<head>
<meta charset="utf-8">
<title>鷹巣岳城 御城印</title>
<link rel="stylesheet" href="https://fonts.googleapis.com/css2?family=Yuji+Boku&family=Zen+Antique&display=swap">
<style>
  :root {
    --page: #ffffff;
    --card-edge: #8a8a8a;
    --cloud-light: #f4f4f4;
    --cloud-mid: #dcdcdc;
    --cloud-dark: #c2c2c2;
    --ink: #151515;
    --crest-red: #d8261f;
    --figure-grey: #cfcfcf;
  }
  html, body {
    margin: 0;
    padding: 0;
    width: 846px;
    height: 1200px;
    overflow: hidden;
    background: var(--page);
  }
  .canvas {
    position: relative;
    width: 846px;
    height: 1200px;
  }
  .seal-card {
    position: absolute;
    left: 219px;
    top: 240px;
    width: 424px;
    height: 652px;
    border: 1.5px solid var(--card-edge);
    box-sizing: border-box;
    overflow: hidden;
    background: var(--page);
  }
  .cloud-backdrop {
    position: absolute;
    inset: 0;
    background:
      radial-gradient(ellipse 55% 22% at 35% 14%, var(--cloud-mid), transparent 70%),
      radial-gradient(ellipse 45% 20% at 20% 45%, var(--cloud-mid), transparent 70%),
      radial-gradient(ellipse 70% 25% at 30% 90%, var(--cloud-mid), transparent 70%),
      linear-gradient(165deg, var(--cloud-light) 0%, var(--page) 40%, var(--cloud-light) 70%, var(--cloud-mid) 100%);
  }
  .family-crest {
    position: absolute;
    left: 12px;
    top: 40px;
    width: 130px;
    height: 130px;
    border-radius: 50%;
    background: var(--crest-red);
  }
  .warrior-figure {
    position: absolute;
    left: 289px;
    top: 374px;
    width: 135px;
    height: 278px;
    border-radius: 60px 40px 0 0;
    background: linear-gradient(180deg, var(--cloud-light), var(--figure-grey));
  }
  .vertical {
    position: absolute;
    writing-mode: vertical-rl;
    text-orientation: upright;
    color: var(--ink);
    margin: 0;
    line-height: 1;
  }
  .designation {
    left: 350px;
    top: 20px;
    font-family: "Zen Antique", serif;
    font-size: 36px;
    letter-spacing: 2px;
  }
  .region {
    left: 286px;
    top: 126px;
    font-family: "Zen Antique", serif;
    font-size: 56px;
    letter-spacing: 8px;
  }
  .castle-name {
    left: 140px;
    top: 194px;
    font-family: "Yuji Boku", serif;
    font-size: 100px;
    font-weight: 400;
    letter-spacing: 2px;
  }
  .date-line {
    left: 40px;
    top: 196px;
    font-family: "Zen Antique", serif;
    font-size: 30px;
  }
  .date-line .unit {
    display: inline-block;
    margin-inline-start: 50px;
  }
</style>
</head>
<body>
<div class="canvas">
  <section class="seal-card">
    <div class="cloud-backdrop" role="img" aria-label="淡い灰色の雲模様の背景"></div>
    <div class="family-crest" role="img" aria-label="朱色の家紋の位置"></div>
    <div class="warrior-figure" role="img" aria-label="甲冑姿の人物像のイラスト"></div>

    <p class="vertical designation">国指定史跡</p>
    <p class="vertical region">対馬</p>
    <h1 class="vertical castle-name">鷹巣岳城</h1>
    <p class="vertical date-line">令和<span class="unit">年</span><span class="unit">月</span><span class="unit">日</span></p>
  </section>
</div>
</body>
</html>
```